Electrical contractor needs a flyer and business card

'Voltmark - The Electrical Contractor' needs an a5 flyer designed which will showcase the work we undertake. We already have a logo - see attached
We operate in Devon and Cornwall in the UK in these 3 market sectors: Domestic, Commercial, Industrial.
The work we undertake is as follows:
House re-wires
New builds
RCD and consumer unit upgrades
Renovations
TV aerials & extra points
Data / phone / networking
Security and garden lighting
Extra external / internal sockets
Garage upgrades
LED and low energy lighting installs
We offer a free consumer unit and earthing check!
24 hour service.
prompt quality service with over 15 years experience
All our work is fully certified and guaranteed for a year
contact details:
Peter Haddow
Owner
peter@voltmark-wiring.co.uk
www.voltmark-wiring.co.uk
m: 07836219087
t: 01392 615 830
Servicing Devon & Cornwall
We also need a business card designed
many thanks
Col
Domestic, Commercial, Industrial.
Contractor
- eurostile extended

```html
<!DOCTYPE html>
<html lang="en">
<head>
<meta charset="utf-8">
<title>Voltmark - The Electrical Contractor</title>
<link href="https://fonts.googleapis.com/css2?family=Arimo:wght@400;700&display=swap" rel="stylesheet">
<style>
  :root{
    --teal:#97cdc8;
    --teal-deep:#2a8ea3;
    --charcoal:#505050;
    --grey:#9ea3a5;
    --text:#454545;
    --white:#ffffff;
    --rule:#b5b8ba;
  }
  html,body{margin:0;padding:0;width:1200px;height:900px;overflow:hidden;background:var(--white);}
  body{font-family:"Arimo",Arial,sans-serif;position:relative;}
  .flyer{position:absolute;left:261px;top:0;width:654px;height:900px;}
  .corner-bar{position:absolute;left:604px;top:0;width:50px;height:200px;background:var(--teal);}
  .logo-box{position:absolute;left:-3px;top:25px;width:422px;height:124px;border:3px solid var(--grey);border-left:none;border-radius:0 12px 12px 0;box-sizing:border-box;}
  .logo{position:absolute;left:34px;top:38px;display:flex;align-items:center;gap:10px;}
  .logo-dot{width:36px;height:36px;border-radius:50%;background:var(--charcoal);}
  .logo-name{font-weight:700;font-size:34px;letter-spacing:6px;color:var(--charcoal);line-height:1;}
  .logo-tag{position:absolute;left:84px;top:70px;font-size:15px;letter-spacing:1px;color:var(--teal-deep);}
  .band{position:absolute;top:201px;height:142px;display:flex;align-items:center;justify-content:center;text-align:center;color:var(--white);font-weight:700;}
  .band-years{left:0;width:234px;background:var(--teal);font-size:30px;line-height:38px;}
  .band-with{left:234px;width:178px;background:var(--charcoal);font-size:66px;}
  .band-quality{left:412px;width:242px;background:var(--grey);font-size:30px;line-height:38px;}
  .side-frames{position:absolute;left:0;top:343px;width:654px;height:395px;}
  .services{position:absolute;left:33px;top:400px;color:var(--text);font-weight:700;}
  .services h2{margin:0 0 34px;font-size:24px;}
  .services ul{list-style:none;margin:0;padding:0;font-size:19px;line-height:24.6px;}
  .divider{position:absolute;left:418px;top:363px;width:1px;height:357px;background:var(--rule);}
  .region{position:absolute;left:445px;top:455px;width:175px;margin:0;font-size:19px;line-height:24.6px;font-weight:700;color:var(--text);}
  .certified{position:absolute;left:0;top:738px;width:398px;height:162px;background:var(--teal);display:flex;align-items:center;justify-content:center;text-align:center;font-size:38px;line-height:48px;font-weight:700;color:var(--text);}
  .bottom-bar{position:absolute;left:603px;top:738px;width:51px;height:162px;background:var(--teal);}
  .connector{position:absolute;left:540px;top:797px;width:64px;height:15px;background:var(--grey);}
  .round-badge{position:absolute;left:412px;top:739px;width:140px;height:140px;border-radius:50%;background:var(--grey);display:flex;align-items:center;justify-content:center;text-align:center;color:var(--white);font-weight:700;font-size:24px;line-height:32px;}
</style>
</head>
<body>
<main class="flyer">
  <div class="corner-bar"></div>
  <div class="logo-box">
    <div class="logo"><span class="logo-dot"></span><span class="logo-name">VOLTMARK</span></div>
    <div class="logo-tag">THE ELECTRICAL CONTRACTOR</div>
  </div>

  <div class="band band-years">15+ YEARS<br>EXPERIENCE</div>
  <div class="band band-with">WITH</div>
  <div class="band band-quality">QUALITY<br>SERVICE</div>

  <svg class="side-frames" viewBox="0 0 654 395" aria-hidden="true">
    <polygon points="0,0 31,0 19,200 31,395 0,395" fill="var(--grey)"/>
    <polygon points="624,0 654,0 654,395 624,395 639,200" fill="var(--grey)"/>
  </svg>

  <section class="services">
    <h2>Services</h2>
    <ul>
      <li>House re-wires</li>
      <li>New builds</li>
      <li>RCD and consumer unit upgrades</li>
      <li>Renovations</li>
      <li>TV aerials &amp; extra points</li>
      <li>Data / phone / networking</li>
      <li>Security and garden lighting</li>
      <li>Extra external / internal sockets</li>
      <li>Garage upgrades</li>
      <li>LED and low energy lighting installs</li>
    </ul>
  </section>
  <div class="divider"></div>
  <p class="region">We operate in Devon and Corn-wall in the UK in these 3 market sectors: Domes-tic, Commercial, Industrial.</p>

  <div class="certified">Fully Certified &amp;<br>Guaranteed</div>
  <div class="bottom-bar"></div>
  <div class="connector"></div>
  <div class="round-badge">24 Hour<br>Service</div>
</main>
</body>
</html>
```